Ledgrix Business Card

We need a business card design using the attached logo. The company is a financial services company that provides a dashboard (chart based information) for Executives of small businesses to use to better manage their information. The design must be progressive, make good utilization of the logo and project stability and financial security.

Industry/Entity Type

Financial

```html
<!DOCTYPE html>
<html lang="en">
<head>
<meta charset="utf-8">
<title>Ledgrix Business Card</title>
<link href="https://fonts.googleapis.com/css2?family=Open+Sans:wght@400;600;700&display=swap" rel="stylesheet">
<style>
  :root {
    --stage: #d9d6d2;
    --card-light: #f4f4f4;
    --card-dark: #0b0b0b;
    --brand-red: #9b1c20;
    --ink: #2b2b2b;
    --ink-soft: #3c3c3c;
    --ghost-light: #e7e7e7;
    --ghost-dark: #262626;
    --white: #ffffff;
  }
  html, body {
    margin: 0;
    padding: 0;
    overflow: hidden;
  }
  body {
    width: 1200px;
    height: 471px;
    background: var(--stage);
    font-family: "Open Sans", Arial, sans-serif;
    position: relative;
  }
  .card {
    position: absolute;
    top: 76px;
    width: 555px;
    height: 318px;
    box-shadow: 0 4px 12px rgba(0,0,0,0.25);
    overflow: hidden;
  }
  .card--front {
    left: 28px;
    background: var(--card-light);
  }
  .card--back {
    left: 615px;
    background: var(--card-dark);
  }
  .ghost-square {
    position: absolute;
    width: 210px;
    height: 210px;
    border-radius: 14px;
  }
  .card--front .ghost-square {
    left: 285px;
    top: 40px;
    background: var(--ghost-light);
  }
  .card--back .ghost-square {
    left: 172px;
    top: 52px;
    background: var(--ghost-dark);
  }
  .brand {
    position: absolute;
    left: 26px;
    top: 68px;
    display: flex;
    align-items: center;
    gap: 10px;
  }
  .brand__mark {
    width: 34px;
    height: 34px;
    background: var(--brand-red);
  }
  .brand__name {
    font-size: 36px;
    font-weight: 600;
    color: var(--ink);
    letter-spacing: -0.5px;
    line-height: 1;
  }
  .contact {
    position: absolute;
    left: 50px;
    top: 232px;
    list-style: none;
    margin: 0;
    padding: 0;
    font-size: 13px;
    color: var(--ink-soft);
  }
  .contact__item {
    display: flex;
    align-items: center;
    gap: 5px;
    height: 22px;
  }
  .contact__item svg {
    width: 12px;
    height: 12px;
    fill: var(--ink-soft);
  }
  .address {
    position: absolute;
    left: 64px;
    top: 290px;
    margin: 0;
    font-size: 15px;
    color: var(--ink-soft);
  }
  .person {
    position: absolute;
    right: 28px;
    top: 250px;
    text-align: right;
  }
  .person__name {
    margin: 0;
    font-size: 17px;
    font-weight: 700;
    color: var(--brand-red);
  }
  .person__role {
    margin: 2px 0 0;
    font-size: 13px;
    font-weight: 600;
    color: #111;
  }
  .back-wordmark {
    position: absolute;
    left: 0;
    right: 0;
    top: 120px;
    text-align: center;
    font-size: 62px;
    font-weight: 700;
    color: var(--white);
    letter-spacing: -1px;
    line-height: 1;
  }
</style>
</head>
<body>
  <section class="card card--front" aria-label="Business card front">
    <div class="ghost-square" aria-hidden="true"></div>
    <div class="brand">
      <span class="brand__mark" aria-hidden="true"></span>
      <span class="brand__name">Ledgrix</span>
    </div>
    <ul class="contact">
      <li class="contact__item">
        <svg viewBox="0 0 24 24" aria-hidden="true"><path d="M6.6 10.8a15.1 15.1 0 0 0 6.6 6.6l2.2-2.2c.3-.3.7-.4 1-.2 1.1.4 2.3.6 3.6.6.6 0 1 .4 1 1V20c0 .6-.4 1-1 1A17 17 0 0 1 3 4c0-.6.4-1 1-1h3.5c.6 0 1 .4 1 1 0 1.3.2 2.5.6 3.6.1.3 0 .7-.2 1z"/></svg>
        123-456-7890
      </li>
      <li class="contact__item">
        <svg viewBox="0 0 24 24" aria-hidden="true"><path d="M2 5h20v14H2z M3.5 6.5 12 13l8.5-6.5" fill="none" stroke="currentColor" stroke-width="0"/><path d="M2 5h20v14H2V5zm2 2v.3l8 5.7 8-5.7V7H4z"/></svg>
        hello@ledgrix.com
      </li>
      <li class="contact__item">
        <svg viewBox="0 0 24 24" aria-hidden="true"><path d="M12 2a10 10 0 1 0 0 20 10 10 0 0 0 0-20zm6.9 6h-2.9a15 15 0 0 0-1.4-3.6A8 8 0 0 1 18.9 8zM12 4c.8 1.2 1.5 2.5 1.9 4h-3.8c.4-1.5 1.1-2.8 1.9-4zM4.3 14a8 8 0 0 1 0-4h3.4a16 16 0 0 0 0 4H4.3zm.8 2h2.9c.3 1.3.8 2.5 1.4 3.6A8 8 0 0 1 5.1 16zM8 8H5.1a8 8 0 0 1 4.3-3.6C8.8 5.5 8.3 6.7 8 8zm4 12c-.8-1.2-1.5-2.5-1.9-4h3.8c-.4 1.5-1.1 2.8-1.9 4zm2.3-6H9.7a14 14 0 0 1 0-4h4.6a14 14 0 0 1 0 4zm.3 5.6c.6-1.1 1.1-2.3 1.4-3.6h2.9a8 8 0 0 1-4.3 3.6zM16.3 14a16 16 0 0 0 0-4h3.4a8 8 0 0 1 0 4h-3.4z"/></svg>
        www.ledgrix.com
      </li>
    </ul>
    <p class="address">Street Name City Name, State Zipcode</p>
    <div class="person">
      <p class="person__name">Your Name</p>
      <p class="person__role">Designation</p>
    </div>
  </section>

  <section class="card card--back" aria-label="Business card back">
    <div class="ghost-square" aria-hidden="true"></div>
    <div class="back-wordmark">Ledgrix</div>
  </section>
</body>
</html>
```